Recruitment Web Site Design

I need a Recruitment website explaining who we are and what services we deliver.
This is a new company and the image we portray is extremely important. Must be very professional.
Our target marget are bluechip companies and professionals including executives.

The final design should communicate connecting professionals matching company and individual needs.

Target Market(s)

Corporate, Blue Chip Companies, Professionals/Executives

Industry/Entity Type

It Company

Requirements
Must have
• Must be professional and Sophisticated.
Must have a few tabs.

Must be unique to the norm of websites as I am looking for something different.
Nice to have
• Good graphics with people connecting. Multi - racial pics will be good as we are in South Africa and diversity is a must.
Also a front page (be unique).

I am putting this out there for you to use your imagination and come up with something brilliant.

A few websites you can base ideas from

www.copperlantern.com
www.ovalquay.co.za
www.kel.co.za
www.rux.co.za

```html
<!DOCTYPE html>
<html lang="en">
<head>
<meta charset="utf-8">
<title>Talvera Recruitment</title>
<link href="https://fonts.googleapis.com/css2?family=Ubuntu:wght@400;500&display=swap" rel="stylesheet">
<style>
  :root{
    --red:#e30613;
    --band:#a9c6ea;
    --grey-light:#d6d6d6;
    --grey-dark:#a8a8a8;
    --tab-blue:#35b3e3;
    --tab-blue-dark:#1e9fd4;
    --accent-blue:#1a9ad6;
    --ink:#1d1d1d;
    --brand-ink:#3a3a3a;
    --white:#ffffff;
  }
  *{margin:0;padding:0;box-sizing:border-box}
  html,body{width:1200px;height:1199px;overflow:hidden;background:var(--white)}
  body{position:relative;font-family:"Ubuntu",sans-serif;color:var(--ink)}
  .abs{position:absolute}

  .main-nav{left:0;top:0;width:1200px;height:40px;display:flex;background:var(--white)}
  .main-nav a{flex:0 0 200px;height:38px;margin-right:1px;display:flex;align-items:center;justify-content:center;
    color:var(--white);font-size:18px;text-decoration:none;
    background:linear-gradient(#c9c9c9,#a9a9a9)}
  .main-nav a:last-child{margin-right:0}
  .main-nav a.is-active{background:var(--red)}

  .hero{left:0;top:40px;width:1200px;height:665px}

  .brand-mark{left:120px;top:296px;width:40px;height:40px;background:var(--red)}
  .brand-name{left:180px;top:294px;font-size:38px;font-weight:400;line-height:44px;color:var(--brand-ink);white-space:nowrap}

  .promo{color:var(--white);width:260px}
  .promo h2{font-size:22px;font-weight:400;margin-bottom:6px}
  .promo p{font-size:14.5px;line-height:19.5px}
  .promo-arrow{width:34px;height:34px}
  .promo-divider{left:396px;top:549px;width:3px;height:119px;background:var(--white)}

  .search-label{left:885px;top:574px;font-size:21px;color:var(--white)}
  .search-field{left:846px;top:603px;width:201px;height:42px;background:var(--white)}
  .search-btn{left:1048px;top:603px;width:101px;height:42px;background:linear-gradient(#c4c4c4,#b0b0b0);
    color:var(--white);font-size:21px;display:flex;align-items:center;justify-content:center}

  .tab-strip{left:0;top:705px;width:1200px;height:70px;background:linear-gradient(var(--grey-dark),var(--grey-light))}
  .tab{top:729px;height:46px;font-size:19px;display:flex;align-items:center;justify-content:center;color:var(--white)}
  .tab.is-active{background:var(--white);color:var(--ink);border-radius:3px 3px 0 0}
  .tab.is-blue{background:linear-gradient(var(--tab-blue),var(--tab-blue-dark));border-radius:3px 3px 0 0}

  .feature-art{left:40px;top:845px;width:280px;height:230px;border-radius:6px;
    background:radial-gradient(ellipse at center,#4a90e0 0%,#8fb9ec 50%,#ffffff 80%)}

  .copy{left:348px;width:395px}
  .copy h3{font-size:22px;font-weight:400;color:var(--ink);margin-bottom:4px}
  .copy h3 .hl{color:var(--accent-blue)}
  .copy h3.blue{color:var(--accent-blue)}
  .copy p{font-size:15px;line-height:19.5px}
  .more-btn{width:83px;height:23px;background:linear-gradient(#e2e2e2,#c8c8c8);color:var(--accent-blue);
    font-size:17px;display:flex;align-items:center;justify-content:center}

  .col-divider{left:842px;top:820px;width:3px;height:282px;background:#cfcfcf}

  .side-tab{top:907px;width:80px;height:28px;border-radius:3px 3px 0 0;background:linear-gradient(var(--tab-blue),var(--tab-blue-dark))}
  .side-box{left:873px;top:934px;width:297px;height:165px;background:#c3c7cb;border-radius:0 0 6px 6px;
    padding:22px 20px;font-size:14.5px;line-height:19.5px}

  .footer-band{left:0;top:1130px;width:1200px;height:69px;background:linear-gradient(#c2c2c2,#d8d8d8)}
</style>
</head>
<body>

<nav class="main-nav abs">
  <a class="is-active" href="#">Home</a>
  <a href="#">About Us</a>
  <a href="#">Services</a>
  <a href="#">Services</a>
  <a href="#">Affilities</a>
  <a href="#">Contect us</a>
</nav>

<svg class="hero abs" viewBox="0 40 1200 665" xmlns="http://www.w3.org/2000/svg">
  <defs>
    <linearGradient id="sky" x1="0" y1="0" x2="0" y2="1">
      <stop offset="0" stop-color="#2e95dc"/>
      <stop offset="1" stop-color="#86d3f3"/>
    </linearGradient>
    <linearGradient id="redFill" gradientUnits="userSpaceOnUse" x1="0" y1="435" x2="0" y2="705">
      <stop offset="0" stop-color="#ee1c1c"/>
      <stop offset="1" stop-color="#cf0a0a"/>
    </linearGradient>
    <linearGradient id="greyFill" gradientUnits="userSpaceOnUse" x1="0" y1="440" x2="0" y2="705">
      <stop offset="0" stop-color="#dcdcdc"/>
      <stop offset="1" stop-color="#b4b4b4"/>
    </linearGradient>
    <linearGradient id="figures" x1="0" y1="0" x2="0" y2="1">
      <stop offset="0" stop-color="#3f7fe0" stop-opacity="0.75"/>
      <stop offset="1" stop-color="#1f5fc8" stop-opacity="0.9"/>
    </linearGradient>
    <clipPath id="leftPart"><rect x="0" y="40" width="797" height="665"/></clipPath>
  </defs>
  <rect x="0" y="40" width="1200" height="665" fill="url(#sky)" role="img" aria-label="Blue sky with soft white clouds"/>
  <path d="M0,365 Q600,610 1200,395 L1200,705 L0,705 Z" fill="var(--band)"/>
  <path d="M0,400 Q600,611 1200,418 L1200,705 L0,705 Z" fill="#ffffff"/>
  <path d="M0,435 Q600,612 1200,440 L1200,705 L0,705 Z" fill="url(#greyFill)"/>
  <path d="M0,435 Q600,612 1200,440 L1200,705 L0,705 Z" fill="url(#redFill)" clip-path="url(#leftPart)"/>
  <rect x="605" y="180" width="440" height="320" rx="20" fill="url(#figures)" role="img" aria-label="Blue figures standing on connected jigsaw pieces"/>
</svg>

<div class="brand-mark abs"></div>
<div class="brand-name abs">Talvera Recruitment</div>

<div class="promo abs" style="left:78px;top:562px">
  <h2>Your Text here</h2>
  <p>Lorem Ipsum is simply dummy text of the printing and typesetting industry. Lorem Ipsum has been the industry's</p>
</div>
<svg class="promo-arrow abs" style="left:341px;top:601px" viewBox="0 0 34 34"><circle cx="17" cy="17" r="17" fill="#fff"/><path d="M14,9 L22,17 L14,25" fill="none" stroke="#e30613" stroke-width="2.5"/></svg>
<div class="promo-divider abs"></div>
<div class="promo abs" style="left:445px;top:562px">
  <h2>Your Text here</h2>
  <p>Lorem Ipsum is simply dummy text of the printing and typesetting industry. Lorem Ipsum has been the industry's</p>
</div>
<svg class="promo-arrow abs" style="left:709px;top:601px" viewBox="0 0 34 34"><circle cx="17" cy="17" r="17" fill="#fff"/><path d="M14,9 L22,17 L14,25" fill="none" stroke="#e30613" stroke-width="2.5"/></svg>

<div class="search-label abs">Search</div>
<div class="search-field abs"></div>
<div class="search-btn abs">Ok</div>

<div class="tab-strip abs"></div>
<div class="tab is-active abs" style="left:56px;width:128px">About Us</div>
<div class="tab abs" style="left:200px;width:128px">Countries</div>
<div class="tab is-blue abs" style="left:341px;width:128px;top:728px;height:47px">Affilities</div>
<div class="tab is-blue abs" style="left:484px;width:128px;top:728px;height:47px">Services</div>

<div class="feature-art abs" role="img" aria-label="Blue figures standing on jigsaw pieces"></div>

<div class="copy abs" style="top:811px">
  <h3><span class="hl">What</span> we do?</h3>
  <p>Lorem Ipsum is simply dummy text of the printing and typesetting industry. Lorem Ipsum has been the industry's standard dummy text ever since the 1500s,</p>
  <p style="margin-top:19px">when an unknown printer took a galley of type and scrambled it to make a type specimen book. It has survived not only five centuries, but also the leap into electronic</p>
</div>
<div class="more-btn abs" style="left:657px;top:985px">More</div>

<div class="copy abs" style="top:1005px">
  <h3 class="blue">Our Services</h3>
  <p>Lorem Ipsum is simply dummy text of the printing and typesetting industry. Lorem Ipsum has been the industry's standard dummy text ever since the 1500s,</p>
</div>
<div class="more-btn abs" style="left:657px;top:1093px">More</div>

<div class="col-divider abs"></div>

<div class="side-tab abs" style="left:880px"></div>
<div class="side-tab abs" style="left:966px"></div>
<div class="side-tab abs" style="left:1051px"></div>
<div class="side-box abs">Lorem Ipsum is simply dummy text of the printing and typesetting industry. Lorem Ipsum has been the industry's standard dummy text ever since the 1500s,</div>

<div class="footer-band abs"></div>

</body>
</html>
```